Business Card Design

Brambleton Energy, L.P. is an energy and lifecycle management firm that creates value in petroleum products through synergistic marketing, trading, recovery, logistics and beneficial reuse services.

Sell top-quality refinery feedstock, petroleum products and co-products on the spot and futures makets (energy trading)

Separate, reclaim and/or manufacture valuable products for beneficial reuse (environmental)
Updates

The tag line Understanding Solutions   Performance are three different concepts and need to be kept either spaced apart or separated in some way. Thanks. 

Target Market(s)

Refiners, Petroleum storage companies, energy marketers

Industry/Entity Type

Business

Contact Information for Business Card

Gwendolyn R. Hask
Principal
Brambleton Energy, L.P.
4817 Quillby St.
Houston, TX 77081
713-482-6619 phone
713-641-8854 fax
g.hask@brambletonenergy-example.com
www.brambletonenergy-example.com

Requirements
Must have
• Tagline outlined in matching orange -

Understanding Solutions Performance
Nice to have
• Coordinating typestyles

```html
<!DOCTYPE html>
<html lang="en">
<head>
<meta charset="utf-8">
<title>Brambleton Energy, L.P. – Business Card</title>
<link href="https://fonts.googleapis.com/css2?family=Open+Sans:wght@400;600;700&display=swap" rel="stylesheet">
<style>
  :root {
    --backdrop: #d9d9d9;
    --card-white: #ffffff;
    --card-black: #1c1c1c;
    --accent-orange: #f05a22;
    --tagline-grey: #3a3a3a;
    --text-light: #ffffff;
    --text-muted: #e6e6e6;
  }
  * { margin: 0; padding: 0; box-sizing: border-box; }
  html, body {
    width: 1200px; height: 893px; overflow: hidden;
    background: var(--backdrop);
    font-family: "Open Sans", Arial, sans-serif;
  }
  .canvas { position: relative; width: 1200px; height: 893px; }

  .card {
    position: absolute;
    width: 540px; height: 310px;
    border-radius: 20px;
    overflow: hidden;
    box-shadow: 0 6px 18px rgba(0,0,0,0.18);
  }

  /* Tagline side */
  .card--back { left: 70px; top: 110px; background: var(--card-white); }
  .tagline {
    position: absolute; inset: 0;
    display: flex; align-items: center; justify-content: center;
    font-size: 22px; letter-spacing: 1.5px; color: var(--tagline-grey);
  }
  .tagline__divider {
    display: inline-block; width: 3px; height: 28px;
    background: var(--accent-orange); margin: 0 10px;
  }

  /* Contact side */
  .card--front { left: 590px; top: 470px; background: var(--card-black); }
  .card__shapes { position: absolute; inset: 0; }
  .brand {
    position: absolute; left: 265px; top: 70px; width: 250px;
    display: flex; align-items: center; gap: 12px;
    color: var(--card-black); font-weight: 700; font-size: 24px; line-height: 1.15;
  }
  .brand__dot { flex: none; width: 30px; height: 30px; border-radius: 50%; background: var(--accent-orange); }

  .person { position: absolute; left: 34px; top: 128px; color: var(--text-light); }
  .person__name { font-weight: 700; font-size: 18px; }
  .person__title { font-size: 14px; color: var(--text-muted); margin-top: 2px; }

  .contact {
    position: absolute; left: 34px; top: 196px;
    list-style: none; color: var(--text-light); font-size: 12px; line-height: 1.5;
  }
  .contact li { display: flex; align-items: flex-start; gap: 7px; }
  .contact__group { margin-bottom: 8px; }
  .contact__icon { flex: none; width: 13px; height: 13px; margin-top: 2px; }
</style>
</head>
<body>
<main class="canvas">

  <section class="card card--back" aria-label="Card back with tagline">
    <p class="tagline">
      Understanding<span class="tagline__divider"></span>Solutions<span class="tagline__divider"></span>Performance
    </p>
  </section>

  <section class="card card--front" aria-label="Card front with contact details">
    <svg class="card__shapes" width="540" height="310" viewBox="0 0 540 310" aria-hidden="true">
      <path d="M168,0 C170,170 320,252 540,214 L540,0 Z" fill="var(--accent-orange)"/>
      <path d="M196,0 C200,150 330,230 540,198 L540,0 Z" fill="var(--card-white)"/>
      <rect x="527" y="48" width="13" height="44" fill="var(--accent-orange)"/>
    </svg>

    <div class="brand">
      <span class="brand__dot"></span>
      <span class="brand__name">Brambleton Energy, L.P.</span>
    </div>

    <div class="person">
      <p class="person__name">Gwendolyn R. Hask</p>
      <p class="person__title">Principal</p>
    </div>

    <ul class="contact">
      <li class="contact__group">
        <svg class="contact__icon" viewBox="0 0 14 14"><circle cx="7" cy="7" r="7" fill="#fff"/><path d="M7 3 L11 7 H9.5 V10.5 H4.5 V7 H3 Z" fill="var(--card-black)"/></svg>
        <span>4817 Quillby St.<br>Houston, TX 77081</span>
      </li>
      <li>
        <svg class="contact__icon" viewBox="0 0 14 14"><circle cx="7" cy="7" r="7" fill="#fff"/><path d="M4 4.5 Q7 2.5 10 4.5 L9.5 6 L8.3 5.6 L8 6.2 H6 L5.7 5.6 L4.5 6 Z M4.5 7 H9.5 L10 10 H4 Z" fill="var(--card-black)"/></svg>
        <span>713-482-6619</span>
      </li>
      <li>
        <svg class="contact__icon" viewBox="0 0 14 14"><circle cx="7" cy="7" r="7" fill="#fff"/><rect x="4" y="4" width="6" height="6.5" fill="var(--card-black)"/><rect x="5" y="5" width="4" height="1.5" fill="#fff"/></svg>
        <span>713-641-8854</span>
      </li>
      <li>
        <svg class="contact__icon" viewBox="0 0 14 14"><circle cx="7" cy="7" r="7" fill="#fff"/><rect x="3.5" y="4.5" width="7" height="5" fill="var(--card-black)"/><path d="M3.5 4.5 L7 7.5 L10.5 4.5" stroke="#fff" stroke-width="0.8" fill="none"/></svg>
        <span>g.hask@brambletonenergy-example.com</span>
      </li>
      <li>
        <svg class="contact__icon" viewBox="0 0 14 14"><circle cx="7" cy="7" r="7" fill="#fff"/><circle cx="7" cy="7" r="3.8" fill="none" stroke="var(--card-black)" stroke-width="0.9"/><path d="M3.2 7 H10.8 M7 3.2 V10.8" stroke="var(--card-black)" stroke-width="0.8"/></svg>
        <span>www.brambletonenergy-example.com</span>
      </li>
    </ul>
  </section>

</main>
</body>
</html>
```